QX27

We want a trendy packaging design for our mobile accessories. Initially we will be offering TPU cases to our retail customers and than we will introduce other similar accessories such as car chargers, AC chargers, data cables etc..
We would like to see designs that are unique, practical and appealing to the general audience.
Updates

Hi Everyone

There is guaranteed payment for the best designer of this packaging.

thanks

Reason: Hi All This will give you all more time to submit your designs :) regards

Target Market(s)

Telco retail store customers

Industry/Entity Type

Retail

Requirements
Must have
• Colorful , Fun , Sexy

```html
<!DOCTYPE html>
<html lang="en">
<head>
<meta charset="utf-8">
<title>Lumora accessories – hang-tab box dieline</title>
<link href="https://fonts.googleapis.com/css2?family=Questrial&display=swap" rel="stylesheet">
<style>
  :root {
    --paper: #ffffff;
    --guide: #a9d8ea;
    --hang-dark: #3f3f3f;
    --hang-mid: #4b4b4b;
    --hang-light: #dcdcdc;
    --red-top: #e20a16;
    --red-mid: #b80d18;
    --red-deep: #7e0b14;
    --window: #ffffff;
    --window-shade: #4a060c;
    --ink-light: #ffffff;
  }
  * { box-sizing: border-box; margin: 0; padding: 0; }
  html, body { width: 1200px; height: 1112px; overflow: hidden; background: var(--paper); }
  body { position: relative; font-family: "Questrial", "Century Gothic", sans-serif; color: var(--ink-light); }

  .box { position: absolute; top: 100px; width: 530px; height: 970px; }
  .box--left { left: 87px; }
  .box--right { left: 617px; }

  .hang-panel {
    position: absolute; left: 0; top: 0; width: 355px; height: 462px;
    background: linear-gradient(180deg, var(--hang-dark) 0%, var(--hang-mid) 42%, #8d8d8d 66%, var(--hang-light) 100%);
  }
  .fold-line { position: absolute; left: 0; width: 100%; height: 1px; background: var(--guide); opacity: .7; }

  .euro-slot { position: absolute; left: 105px; width: 146px; height: 42px; }

  .brand { position: absolute; left: 0; top: 335px; width: 355px; text-align: center; }
  .brand__name { font-size: 64px; line-height: 1; letter-spacing: 1px; }
  .brand__tag { font-size: 27px; letter-spacing: 9px; margin-top: 2px; }

  .front-panel {
    position: absolute; left: 0; top: 462px; width: 355px; height: 508px; overflow: hidden;
  }
  .side-panel {
    position: absolute; left: 355px; top: 462px; width: 175px; height: 508px; overflow: hidden;
    border-left: 1px solid rgba(169,216,234,.5);
  }
  .red-field {
    position: absolute; inset: 0;
    background:
      radial-gradient(ellipse at 30% 20%, rgba(255,60,60,.25), transparent 60%),
      linear-gradient(180deg, var(--red-top) 0%, var(--red-mid) 45%, var(--red-deep) 100%);
  }
  .side-flap-top {
    position: absolute; left: 355px; top: 275px; width: 175px; height: 187px;
    border: 1px solid var(--guide); border-bottom: none;
  }

  .panel-text { position: absolute; left: 25px; font-size: 24px; white-space: nowrap; }
  .panel-text--top { top: 40px; }
  .panel-text--bottom { top: 445px; }

  .product-window { position: absolute; left: 55px; top: 60px; width: 300px; height: 380px; }

  .side-brand {
    position: absolute; left: 50%; top: 50%; width: 420px; text-align: center;
    transform: translate(-50%, -50%) rotate(-90deg);
  }
  .side-brand .brand__name { font-size: 66px; }
  .side-brand .brand__tag { font-size: 28px; letter-spacing: 10px; }
</style>
</head>
<body>

  <section class="box box--left">
    <div class="hang-panel">
      <svg class="euro-slot" style="top:55px" viewBox="0 0 146 42" aria-hidden="true">
        <path d="M16 12 H58 A15 12 0 0 1 88 12 H130 A14 14 0 0 1 130 40 H16 A14 14 0 0 1 16 12 Z" fill="#fff"/>
      </svg>
      <div class="fold-line" style="top:137px"></div>
      <svg class="euro-slot" style="top:190px" viewBox="0 0 146 42" aria-hidden="true">
        <path d="M16 12 H58 A15 12 0 0 1 88 12 H130 A14 14 0 0 1 130 40 H16 A14 14 0 0 1 16 12 Z" fill="#fff"/>
      </svg>
      <div class="brand">
        <div class="brand__name">Lumora</div>
        <div class="brand__tag">accessories</div>
      </div>
    </div>
    <div class="side-flap-top"></div>
    <div class="front-panel">
      <div class="red-field" role="img" aria-label="Red gradient backdrop with scattered square pattern"></div>
      <p class="panel-text panel-text--top">Your text</p>
      <svg class="product-window" viewBox="0 0 300 380" aria-hidden="true">
        <rect x="62" y="40" width="180" height="295" rx="42" transform="rotate(22 152 188)" fill="var(--window-shade)" opacity=".8"/>
        <rect x="56" y="36" width="180" height="295" rx="42" transform="rotate(22 146 184)" fill="var(--window)"/>
      </svg>
      <p class="panel-text panel-text--bottom">Your text Your textYour text</p>
    </div>
    <div class="side-panel">
      <div class="red-field" role="img" aria-label="Red gradient backdrop with scattered square pattern"></div>
      <div class="side-brand">
        <div class="brand__name">Lumora</div>
        <div class="brand__tag">accessories</div>
      </div>
    </div>
  </section>

  <section class="box box--right">
    <div class="hang-panel">
      <div class="fold-line" style="top:80px"></div>
      <div class="brand">
        <div class="brand__name">Lumora</div>
        <div class="brand__tag">accessories</div>
      </div>
    </div>
    <div class="side-flap-top"></div>
    <div class="front-panel">
      <div class="red-field" role="img" aria-label="Red gradient backdrop with scattered square pattern"></div>
      <p class="panel-text panel-text--top">Your text</p>
      <svg class="product-window" viewBox="0 0 300 380" aria-hidden="true">
        <rect x="62" y="40" width="180" height="295" rx="42" transform="rotate(22 152 188)" fill="var(--window-shade)" opacity=".8"/>
        <rect x="56" y="36" width="180" height="295" rx="42" transform="rotate(22 146 184)" fill="var(--window)"/>
      </svg>
      <p class="panel-text panel-text--bottom">Your text Your textYour text</p>
    </div>
    <div class="side-panel">
      <div class="red-field" role="img" aria-label="Red gradient backdrop with scattered square pattern"></div>
      <div class="side-brand">
        <div class="brand__name">Lumora</div>
        <div class="brand__tag">accessories</div>
      </div>
    </div>
  </section>

</body>
</html>
```